The project is a book cover for a health/recipe book for both Kindle and a future soft cover. Title is Morning Garden Table: Gather Greens and Steady Your Days with a subtitle Six Weeks of Gentle Kitchen Habits. I am a registed dietitian nutritionist specializing in midlife and senior women to help them look and feel 10 years younger by balancing hormones and curbing inflammationI like the idea of fresh colorful whole foods on the cover with a natural clean look. But I am also open to a cover which expresses vitality--perhaps a woman or couple whose "being" expresses energy and vitality.Since I am unsure right at this moment the exact # of pages for the book, I will need to have some wiggle room in the final stages to get the spine dimensions.I am happy to send a table of contents if that would help.I need to decide on a cover in the next 2 weeks. Below are some ideas on style that I like with reservations. Background on 1 is too dark, 2 is too pastel and 3 is good but doesn't move me as much and my followers liked it the least
Updates
Entered wrong completion date and would like more entries.
Target Market(s)
Woman 40 to 65+, college educated
Industry/Entity Type
Nutrition
Colors
Designer to choose colors to be used in the design.
Look and feel
Each slider illustrates characteristics of the customer's brand and the style your logo design should communicate.

```html
<!DOCTYPE html>
<html lang="en">
<head>
<meta charset="utf-8">
<title>Morning Garden Table — Cover Wrap</title>
<link rel="stylesheet" href="https://fonts.googleapis.com/css2?family=Montserrat:wght@500;600;700;800&family=EB+Garamond:wght@400&display=swap">
<style>
  :root {
    --page-bg: #eeeeee;
    --paper: #ffffff;
    --title-brown: #5a1a0a;
    --body-brown: #6a2a14;
    --ink: #111111;
    --citrus-light: #f9a93f;
    --citrus-mid: #f08a24;
    --citrus-deep: #d9570c;
    --on-citrus: #ffffff;
  }
  html, body {
    margin: 0;
    padding: 0;
    width: 899px;
    height: 1200px;
    overflow: hidden;
    background: var(--page-bg);
  }
  .cover-wrap {
    position: absolute;
    left: 11px;
    top: 296px;
    width: 877px;
    height: 608px;
    background: var(--paper);
    overflow: hidden;
  }
  /* Back cover */
  .back-title {
    position: absolute;
    left: 33px;
    top: 120px;
    margin: 0;
    font-family: "Montserrat", sans-serif;
    font-weight: 800;
    color: var(--title-brown);
    line-height: 0.95;
  }
  .back-title .line-main { display: block; font-size: 46px; letter-spacing: -0.5px; }
  .back-title .line-sub { display: block; font-size: 29px; font-weight: 700; }
  .back-blurb {
    position: absolute;
    left: 33px;
    top: 214px;
    width: 342px;
    margin: 0;
    font-family: "EB Garamond", serif;
    font-size: 14.6px;
    line-height: 17.4px;
    color: var(--body-brown);
    text-align: justify;
    hyphens: auto;
  }
  /* Spine */
  .spine-title {
    position: absolute;
    left: 441px;
    top: 144px;
    transform: translate(-50%, -50%) rotate(-90deg);
    font-family: "Montserrat", sans-serif;
    font-weight: 800;
    color: var(--title-brown);
    line-height: 0.95;
    white-space: nowrap;
  }
  .spine-title .line-main { display: block; font-size: 30px; }
  .spine-title .line-sub { display: block; font-size: 20px; font-weight: 700; }
  .spine-author {
    position: absolute;
    left: 440px;
    top: 450px;
    transform: translate(-50%, -50%) rotate(-90deg);
    font-family: "Montserrat", sans-serif;
    font-weight: 600;
    font-size: 12px;
    letter-spacing: 14px;
    color: var(--ink);
    white-space: nowrap;
  }
  /* Front cover */
  .front-art {
    position: absolute;
    left: 545px;
    top: 40px;
    width: 278px;
    height: 516px;
  }
  .front-title {
    position: absolute;
    left: 545px;
    top: 40px;
    width: 278px;
    height: 516px;
    margin: 0;
    font-family: "Montserrat", sans-serif;
    color: var(--on-citrus);
  }
  .front-title span {
    position: absolute;
    left: 0;
    width: 100%;
    text-align: center;
    white-space: nowrap;
  }
  .front-title .t1 { top: 40px; font-size: 42px; font-weight: 800; transform: rotate(-2deg); }
  .front-title .t2 { top: 124px; font-size: 27px; font-weight: 800; transform: rotate(-4deg); }
  .front-subtitle .s1 { top: 230px; font-size: 19px; font-weight: 600; transform: rotate(-8deg); }
  .front-subtitle .s2 { top: 322px; font-size: 16px; font-weight: 600; transform: rotate(-8deg); }
  .front-subtitle .s3 { top: 406px; font-size: 16px; font-weight: 600; transform: rotate(3deg); }
  .front-subtitle .s4 { top: 468px; font-size: 16px; font-weight: 600; letter-spacing: 4px; transform: rotate(4deg); }
  .front-author {
    position: absolute;
    left: 489px;
    top: 572px;
    width: 372px;
    font-family: "Montserrat", sans-serif;
    font-weight: 700;
    font-size: 20px;
    letter-spacing: 17px;
    color: var(--ink);
    white-space: nowrap;
  }
</style>
</head>
<body>
  <main class="cover-wrap">
    <section class="back-cover">
      <h2 class="back-title">
        <span class="line-main">MORNING</span>
        <span class="line-sub">GARDEN TABLE</span>
      </h2>
      <p class="back-blurb">Lorem ipsum dolor sit amet, consectetur adipiscing elit. Cras orci mauris, ullamcorper non varius ac, placerat nec diam. Vestibulum pellentesque, felis ac lobortis finibus, nulla ipsum iaculis nibh, nec blandit elit velit quis neque. Nunc vel massa cursus, ultricies ligula id, consequat elit. Etiam sodales quam vel mi faucibus, ac rutrum erat sodales. Etiam aliquam et lorem eu blandit. Proin auctor orci eget est sodales feugiat. Sed luctus, justo ut maximus varius, libero ipsum ornare tellus, id sollicitudin urna neque egestas lorem. Donec posuere nec dolor vel pretium. Quisque tempor bibendum diam, in placerat nisl. Maecenas eu ullamcorper odio, vel rutrum orci. Mauris sit amet nisl varius, consectetur justo ac, finibus neque. Aenean tincidunt tellus ut leo viverra, ac tristique diam semper.</p>
    </section>

    <section class="spine">
      <div class="spine-title">
        <span class="line-main">MORNING</span>
        <span class="line-sub">GARDEN TABLE</span>
      </div>
      <div class="spine-author">AUTHOR NAME</div>
    </section>

    <section class="front-cover">
      <svg class="front-art" viewBox="0 0 278 516" role="img" aria-label="Photograph of a stack of floating orange slices carrying the title lines">
        <defs>
          <linearGradient id="citrus" x1="0" y1="0" x2="1" y2="1">
            <stop offset="0" stop-color="var(--citrus-light)"/>
            <stop offset="0.55" stop-color="var(--citrus-mid)"/>
            <stop offset="1" stop-color="var(--citrus-deep)"/>
          </linearGradient>
        </defs>
        <rect x="0" y="0" width="278" height="516" rx="40" fill="url(#citrus)"/>
      </svg>
      <h1 class="front-title">
        <span class="t1">MORNING</span>
        <span class="t2">GARDEN TABLE</span>
        <span class="front-subtitle">
          <span class="s1">GATHER GREENS</span>
          <span class="s2">AND STEADY YOUR DAYS</span>
          <span class="s3">SIX WEEKS OF GENTLE</span>
          <span class="s4">KITCHEN HABITS</span>
        </span>
      </h1>
      <div class="front-author">AUTHOR NAME</div>
    </section>
  </main>
</body>
</html>
```